Food Safety 1-California workers only

3.25" by 4.5" Black and White Magazine Ad
This ad is to train California workers only.
Workers will be trained on: Food Safety, FSMA (Food Safety Modernization Act), using equipment safety, food processing production skills, worker safety, supervisory skills, communication skills.
"FREE TRAINING", The company does the training or Keystone Learning will provide the training.
Training grants range from $100,000 to $400,000.
Companies must be in business for profit.
Companies must train 200 employees or more.
This program is for California workers only.
Incumbent or new-hires are eligible.

Target Market(s)

California food processors, farms, food packaging, food processors, companies under FSMA, food safety, food production who need to train employees.

Industry/Entity Type

Food Production

Font styles to use
Serif
Sans Serif

Colors

Designer to choose colors to be used in the design.

Requirements
Must have
• This is a 3.25 inch by 4.5 inch magazine ad. It must be black and white. No color.
• The deliverable must be in basic PhotoShop. The ad does not need to include any graphics and be text only if needed. If you have a black and white graphic that will show well.
• Look at www.KLGFoodSafety..com
• Use the text from "MEALBOX-Photoshop-052018" file as your starting point.
Nice to have
• A black and white graphic about food. See www.KLGFoodSafety.com
Should not have
• No color.

```html
<!DOCTYPE html>
<html lang="en">
<head>
<meta charset="utf-8">
<title>Free Training – Keystone Learning</title>
<link rel="stylesheet" href="https://fonts.googleapis.com/css2?family=Oswald:wght@700&family=Tinos:wght@700&family=Lato:wght@400;900&display=swap">
<style>
  :root {
    --mat: #3c3c3e;
    --ink: #050505;
    --paper: #ffffff;
  }
  * { margin: 0; padding: 0; box-sizing: border-box; }
  html, body { width: 914px; height: 1200px; overflow: hidden; background: var(--mat); }
  .ad {
    position: absolute; left: 118px; top: 132px;
    width: 677px; height: 936px;
    background: var(--paper); overflow: hidden;
  }
  .ad-shapes { position: absolute; inset: 0; }
  .headline {
    position: absolute; left: 0; right: 0; top: 30px;
    text-align: center; color: var(--paper);
    font: 700 102px/1 'Oswald', sans-serif; letter-spacing: 1px;
  }
  .topics {
    position: absolute; left: 0; right: 0; top: 160px; height: 48px;
    background: var(--paper); color: var(--ink);
    display: flex; align-items: center; justify-content: center;
    font: 700 21px/1 'Oswald', sans-serif; letter-spacing: 0.2px;
  }
  .tagline {
    position: absolute; left: 0; right: 0; top: 224px;
    text-align: center; color: var(--paper);
    font: 700 56px/64px 'Oswald', sans-serif;
  }
  .qualify { position: absolute; left: 80px; top: 418px; color: var(--ink); font-family: 'Tinos', serif; }
  .qualify h2 { font-size: 30px; font-weight: 700; margin-bottom: 8px; }
  .qualify ul { list-style: none; }
  .qualify li { font-size: 21px; font-weight: 700; line-height: 27.8px; }
  .qualify li::before { content: "\2022\00a0"; }
  .contact-label {
    position: absolute; left: 240px; width: 199px; top: 711px;
    text-align: center; color: var(--ink);
    font: 900 25px/30px 'Lato', sans-serif;
  }
  .contact {
    position: absolute; top: 779px; left: 0; right: 0;
    display: flex; color: var(--paper);
    font: 400 21px/27.6px 'Lato', sans-serif;
  }
  .contact-address { width: 356px; text-align: right; }
  .contact-links { padding-left: 17px; }
</style>
</head>
<body>
  <main class="ad">
    <svg class="ad-shapes" width="677" height="936" viewBox="0 0 677 936" aria-hidden="true">
      <path d="M0 0 H677 V340 Q338.5 452 0 340 Z" fill="var(--ink)"/>
      <path d="M0 756 Q338.5 660 677 756 V936 H0 Z" fill="var(--ink)"/>
      <polygon points="240,700 439,700 426,752 254,752" fill="var(--paper)"/>
    </svg>

    <h1 class="headline">FREE TRAINING</h1>
    <p class="topics">FOOD SAFETY (FSMA) PRODUCTION SKILLS WORKER SAFETY</p>
    <p class="tagline">“WE DO THE TRAINING AND<br>THE STATE PAYS FOR IT!”</p>

    <section class="qualify">
      <h2>How to Qualify:</h2>
      <ul>
        <li>Train California Workers Only</li>
        <li>Trainees must earn $11/hour</li>
        <li>Full-time workers only</li>
        <li>Employees must attend at least 8 Hours of training</li>
        <li>You must train 200 or more employees</li>
        <li>Incumbent or New-Hire workers are eligible</li>
        <li>Seasonal workers are eligibl</li>
      </ul>
    </section>

    <p class="contact-label">CONTACT:</p>
    <section class="contact">
      <address class="contact-address" style="font-style:normal">
        Daniel Marsh<br>
        Keystone Learning Company, Inc.<br>
        1200 Harbor Crest Drive,<br>
        Suite 310, Irvine, CA 92614
      </address>
      <div class="contact-links">
        www.KLGCAL.com<br>
        www.KLGFoodSafety.com<br>
        Dan.Marsh@KLGCAL.com<br>
        Phone: (949) 555-0148
      </div>
    </section>
  </main>
</body>
</html>
```